Talent Management Company Needs Business Cards

Using one of the logos provided (attached) K&R Talent Collective needs a business card designed.
Please visit our website for more information about us-

www.krtalentcollective.example

The face should feature a dramatic presentation of the logo with the back being reserved for our professional information which is:

The information should be:
Dorian T. Vickers
C.E.O
Email: dtvickers@krtalentcollective.example
Mobile: 555-804-2917
Website: www.krtalentcollective.example

Marcus L. Vickers
Director of Public Relations
Email: mlvickers@krtalentcollective.example
Mobile: 555-806-3350

Jules R. Hampton
Director of Client Development
Email: jhampton@krtalentcollective.example

Simon Hurlock
Director of Brand Development
Email: shurlock@krtalentcollective.example

Would like the logo to have color. I would like to see one side red or black and the other side white but if it looks better in either black or red that would be fine to but would like to see how it comes out.

Please feel free to message me and if you would like just the icon alone I have other image files that I can send as well.

Target Market(s)

Professional Athletes, coaches, entertainers age 18-35 but also must be accepted in the business community

Industry/Entity Type

Business

Requirements
Must have
• 1) Use the logo
2) Double sided
3) Distinctive
Nice to have
• Small simple images for telephone, e-mail, and Url.

```html
<!DOCTYPE html>
<html lang="en">
<head>
<meta charset="utf-8">
<title>K&amp;R Talent Collective — Business Card</title>
<link rel="stylesheet" href="https://fonts.googleapis.com/css2?family=Jost:ital,wght@0,400;0,500;1,400&display=swap">
<style>
  :root {
    --page-bg: #ffffff;
    --red-bright: #dc1a22;
    --red-mid: #b8121a;
    --red-deep: #8a0a0f;
    --card-black: #000000;
    --text-white: #ffffff;
    --accent-red: #e0141e;
    --label-ink: #111111;
  }
  * { margin: 0; padding: 0; box-sizing: border-box; }
  html, body {
    width: 1200px; height: 926px; overflow: hidden;
    background: var(--page-bg);
    font-family: "Jost", "Futura", sans-serif;
  }
  .sheet { position: relative; width: 1200px; height: 926px; }

  .card {
    position: absolute; top: 97px;
    width: 473px; height: 732px;
    overflow: hidden;
  }
  .card--front { left: 116px; }
  .card--back { left: 625px; background: var(--card-black); color: var(--text-white); }

  .front-texture {
    position: absolute; inset: 0;
    background: linear-gradient(180deg, var(--red-bright) 0%, var(--red-mid) 55%, var(--red-deep) 100%);
  }
  .front-brand {
    position: absolute; left: 250px; top: 62px; width: 176px;
    display: flex; flex-direction: column; align-items: center; gap: 12px;
    color: var(--text-white); text-align: center;
    font-size: 24px; font-weight: 500; line-height: 1.15;
  }
  .front-brand__mark {
    width: 44px; height: 44px; background: var(--text-white);
  }

  .back-brand {
    position: absolute; left: 0; right: 0; top: 110px;
    display: flex; flex-direction: column; align-items: center; gap: 46px;
  }
  .back-brand__mark {
    width: 80px; height: 80px; border-radius: 50%; background: var(--accent-red);
  }
  .back-brand__name {
    font-size: 30px; font-weight: 400; line-height: 1; color: var(--text-white);
    letter-spacing: 0.5px; text-transform: uppercase;
  }

  .person { position: absolute; left: 54px; top: 386px; }
  .person__name { font-size: 22px; font-weight: 500; letter-spacing: 0.6px; line-height: 28px; }
  .person__title { font-size: 21px; font-style: italic; line-height: 28px; }

  .contact { position: absolute; left: 54px; top: 485px; list-style: none; font-size: 18px; line-height: 27px; }
  .contact__key { color: var(--accent-red); font-weight: 500; display: inline-block; width: 26px; }

  .address { position: absolute; left: 54px; top: 603px; font-size: 18.5px; line-height: 25px; font-style: normal; }

  .side-label {
    position: absolute; top: 848px; width: 473px; text-align: center;
    font-size: 34px; font-weight: 500; color: var(--label-ink);
  }
  .side-label--front { left: 116px; }
  .side-label--back { left: 625px; }
</style>
</head>
<body>
<main class="sheet">
  <section class="card card--front" aria-label="Card front">
    <div class="front-texture" role="img" aria-label="Red gradient background with a subtle repeating star pattern"></div>
    <div class="front-brand">
      <span class="front-brand__mark"></span>
      <span>K&amp;R Talent Collective</span>
    </div>
  </section>

  <section class="card card--back" aria-label="Card back">
    <div class="back-brand">
      <span class="back-brand__mark"></span>
      <span class="back-brand__name">K&amp;R Talent Collective</span>
    </div>

    <div class="person">
      <p class="person__name">Dorian T. Vickers</p>
      <p class="person__title">CEO</p>
    </div>

    <ul class="contact">
      <li><span class="contact__key">T :</span> 555-804-2917</li>
      <li><span class="contact__key">E :</span> dtvickers@krtalentcollective.example</li>
      <li><span class="contact__key">W:</span> www.krtalentcollective.example</li>
    </ul>

    <address class="address">
      2710 Harlow Crest Ave<br>
      Suite 410, Brookfield, OH 45099
    </address>
  </section>

  <p class="side-label side-label--front">Front</p>
  <p class="side-label side-label--back">Back</p>
</main>
</body>
</html>
```